Tidal Pastry Depot Business card

We are empanada whole-sellers and I want a business card design with a picture of an empanada on it that also mentions first trial order FREE. our contact number 555-274-1193 our website www.zarifaban.com and business email Tomas@zarifaban.com

If you want any of our artwork please feel free to email me at the address above.

```html
<!DOCTYPE html>
<html lang="en">
<head>
<meta charset="utf-8">
<title>Tidal Pastry Depot – Business Card</title>
<link rel="stylesheet" href="https://fonts.googleapis.com/css2?family=Jost:wght@500;700&display=swap">
<style>
  :root {
    --card-yellow: #f7e613;
    --ink-black: #1d1d1b;
    --pastry-dark: #a8441a;
    --pastry-mid: #c8621f;
    --pastry-light: #d47a2c;
  }
  html, body {
    margin: 0;
    padding: 0;
    width: 1200px;
    height: 775px;
    overflow: hidden;
    background: #ffffff;
  }
  .card {
    position: relative;
    width: 1200px;
    height: 775px;
    background: var(--card-yellow);
    border-radius: 16px;
    overflow: hidden;
    font-family: "Jost", "Helvetica Neue", Arial, sans-serif;
  }
  .card__backdrop {
    position: absolute;
    inset: 0 0 116px 0;
    background: linear-gradient(180deg, #f8e81a 0%, #f5dc16 100%);
  }
  .brand-name {
    position: absolute;
    top: 150px;
    left: 0;
    width: 100%;
    margin: 0;
    text-align: center;
    font-weight: 700;
    font-size: 104px;
    line-height: 1;
    color: var(--ink-black);
    letter-spacing: 1px;
  }
  .pastry-illustration {
    position: absolute;
    left: 334px;
    top: 300px;
    width: 532px;
    height: 270px;
    border-radius: 12px;
    background: linear-gradient(180deg, var(--pastry-light) 0%, var(--pastry-mid) 60%, var(--pastry-dark) 100%);
  }
  .contact-line {
    position: absolute;
    top: 596px;
    left: 0;
    width: 100%;
    margin: 0;
    display: flex;
    justify-content: center;
    gap: 44px;
    font-weight: 500;
    font-size: 26px;
    line-height: 36px;
    color: var(--ink-black);
  }
  .offer-band {
    position: absolute;
    left: 0;
    bottom: 0;
    width: 100%;
    height: 116px;
    background: var(--ink-black);
    display: flex;
    align-items: center;
    justify-content: center;
  }
  .offer-band__text {
    margin: 0;
    color: var(--card-yellow);
    font-weight: 500;
    font-size: 60px;
    letter-spacing: 8.5px;
    text-transform: uppercase;
    white-space: nowrap;
  }
</style>
</head>
<body>
  <main class="card">
    <div class="card__backdrop" role="img" aria-label="Yellow background scattered with short orange sprinkle dashes"></div>
    <h1 class="brand-name">Tidal Pastry Depot</h1>
    <div class="pastry-illustration" role="img" aria-label="Illustration of a golden-brown baked empanada with a crimped edge"></div>
    <p class="contact-line">
      <span class="contact-line__phone">555-274-1193</span>
      <span class="contact-line__web">www.zarifaban.com</span>
      <span class="contact-line__email">Tomas@zarifaban.com</span>
    </p>
    <div class="offer-band">
      <p class="offer-band__text">First Trial Order Free</p>
    </div>
  </main>
</body>
</html>
```